Re-design of current business cards

We are updating our website with new colors and layout. Would like to re-design our business cards to co-ordinate. See attached pdf with new Brindlecraft website colors. We would also like to combine our 2 brands on the one business card. Attached is the new design for our Brindlecraft website, current business cards, which are one sided, brindlecraft logo in tiff, .ai for fonts. Brindlecraft logo font is Optimum, Quillmarsh website home page image, Quillmarsh brand statics for products which includes the logo for this brand.

Quillmarsh brand will stay the dark gray on the website. See attached statics for product and website home page.
Updates

The business cards will be 2 sided. Brindlecraft Brand on one side and Quillmarsh Brand on the other. The colors for Brindlecraft need to follow the color scheme of the brindlecraft website pdf I uploaded. The colors are a blue, lighter teal blue and white. Quillmarsh needs to follow the dark gray color on files uploaded

Target Market(s)

The trade and consumers

Industry/Entity Type

Home Furnishing

Contact Information for Business Card

We are updating our website with new colors and layout. Would like to re-design our business cards to co-ordinate. We would also like to combine our 2 brands onto 1 2 sided business cards.

Requirements
Must have
• Colors that match our new website, see attached image.
• RGB colors
• navy -#152842
• teal - 98aeb9
• The gray color used for Quillmarsh brands.
• ll logos and fonts should stay the same.

```html
<!DOCTYPE html>
<html lang="en">
<head>
<meta charset="utf-8">
<title>Brindlecraft &amp; Quillmarsh Business Card</title>
<link href="https://fonts.googleapis.com/css2?family=Tinos:wght@400;700&family=Mulish:wght@400;700;800&display=swap" rel="stylesheet">
<style>
  :root {
    --navy: #152842;
    --navy-light: #1f3a5e;
    --navy-deep: #0f1e33;
    --teal: #98aeb9;
    --charcoal: #444444;
    --charcoal-light: #5e5e5e;
    --charcoal-deep: #3c3c3c;
    --magenta: #d018d6;
    --ink: #111111;
    --paper: #ffffff;
    --soft-text: #e9e9e9;
  }
  * { margin: 0; padding: 0; box-sizing: border-box; }
  html, body { width: 1040px; height: 1200px; overflow: hidden; background: var(--paper); }
  .canvas { position: relative; width: 1040px; height: 1200px; }

  /* ---------- Brindlecraft side: brand panel ---------- */
  .brand-side {
    position: absolute; left: 6px; top: 0; width: 367px; height: 600px;
    background: var(--paper);
    border-left: 2px solid var(--ink);
    border-right: 4px solid var(--ink);
    font-family: "Mulish", sans-serif;
  }
  .brand-mark {
    position: absolute; left: 106px; top: 180px; width: 150px; height: 150px;
    border-radius: 50%; background: var(--navy);
  }
  .brand-divider { position: absolute; top: 340px; height: 2px; background: var(--teal); }
  .brand-divider.left { left: 29px; width: 113px; }
  .brand-divider.right { left: 228px; width: 103px; }
  .brand-stars {
    position: absolute; top: 330px; left: 160px; width: 50px; text-align: center;
    color: var(--navy); font-size: 16px; letter-spacing: 1px;
  }
  .company-name {
    position: absolute; top: 364px; left: 0; width: 361px; text-align: center;
    font-size: 25px; font-weight: 400; color: var(--ink); letter-spacing: 0.5px;
  }
  .person-name {
    position: absolute; top: 398px; left: 0; width: 361px; text-align: center;
    font-size: 22px; color: var(--ink);
  }
  .person-name .first { color: var(--navy); font-weight: 800; }
  .person-title {
    position: absolute; top: 427px; left: 0; width: 361px; text-align: center;
    font-size: 21px; font-weight: 800; line-height: 28px; color: var(--ink);
  }

  /* ---------- Brindlecraft side: contact panel ---------- */
  .contact-side {
    position: absolute; left: 373px; top: 4px; width: 667px; height: 596px;
    background: radial-gradient(ellipse at 50% 55%, var(--navy-light) 0%, var(--navy) 60%, var(--navy-deep) 100%);
    font-family: "Tinos", serif; color: var(--paper);
  }
  .web-band {
    position: absolute; left: 0; top: 74px; width: 667px; height: 46px;
    background: var(--paper);
    display: flex; align-items: center; justify-content: center;
    font-size: 27px; font-weight: 700; color: var(--navy); letter-spacing: 0.5px;
  }
  .contact-row { position: absolute; left: 45px; width: 600px; }
  .contact-icon {
    position: absolute; left: 0; top: 0; width: 64px; height: 64px; border-radius: 50%;
    background: var(--teal); display: flex; align-items: center; justify-content: center;
  }
  .contact-text { position: absolute; left: 98px; font-size: 24px; line-height: 43px; letter-spacing: 0.3px; white-space: nowrap; }
  .contact-rule { position: absolute; left: 49px; width: 594px; height: 2px; background: var(--teal); }

  /* ---------- Quillmarsh side ---------- */
  .collection-side {
    position: absolute; left: 0; top: 604px; width: 1040px; height: 580px;
    background: radial-gradient(ellipse at 50% 50%, var(--charcoal-light) 0%, var(--charcoal) 55%, var(--charcoal-deep) 100%);
    font-family: "Tinos", serif; color: var(--soft-text); text-align: center;
  }
  .mirror-frame-art {
    position: absolute; left: 348px; top: 18px; width: 360px; height: 520px;
    border-radius: 45% 45% 40% 40%;
    background: radial-gradient(ellipse at 50% 50%, rgba(255,255,255,0) 40%, rgba(130,118,118,0.08) 75%, rgba(80,80,80,0) 100%);
  }
  .intro-label { position: absolute; top: 130px; left: 0; width: 1040px; font-size: 20px; letter-spacing: 0.8px; }
  .collection-name { position: absolute; top: 155px; left: 0; width: 1040px; font-size: 48px; color: var(--magenta); letter-spacing: 1px; }
  .collection-rule { position: absolute; top: 242px; height: 1px; background: var(--soft-text); }
  .collection-rule.left { left: 203px; width: 287px; }
  .collection-rule.right { left: 562px; width: 258px; }
  .collection-stars { position: absolute; top: 230px; left: 490px; width: 72px; font-size: 18px; letter-spacing: 1px; }
  .collection-features { position: absolute; top: 272px; left: 0; width: 1040px; font-size: 21px; line-height: 27px; letter-spacing: 0.4px; }
  .collection-dates { position: absolute; top: 368px; left: 0; width: 1040px; font-size: 21px; line-height: 26.5px; letter-spacing: 0.4px; }
</style>
</head>
<body>
<main class="canvas">

  <section class="brand-side">
    <div class="brand-mark"></div>
    <div class="brand-divider left"></div>
    <div class="brand-stars">***</div>
    <div class="brand-divider right"></div>
    <div class="company-name">THE BRINDLECRAFT CO.</div>
    <div class="person-name"><span class="first">MARLA</span> TEAGUE</div>
    <div class="person-title">GRAPHIC/PHOTOGRAPHIC<br>DIRECTOR</div>
  </section>

  <section class="contact-side">
    <div class="web-band">HTTP://WWW.BRINDLECRAFT.COM</div>

    <div class="contact-row" style="top:178px;">
      <div class="contact-icon">
        <svg width="30" height="36" viewBox="0 0 30 36"><path d="M15 1C7.8 1 2 6.6 2 13.5 2 23 15 35 15 35s13-12 13-21.5C28 6.6 22.2 1 15 1z" fill="#152842"/><circle cx="15" cy="13" r="5" fill="#98aeb9"/></svg>
      </div>
      <div class="contact-text" style="top:-4px;">PO BOX 412/1870 FERNBROOK MILL ROAD<br>HOLLINS FORD ,VIRGINIA 24099.</div>
    </div>
    <div class="contact-rule" style="top:273px;"></div>

    <div class="contact-row" style="top:300px;">
      <div class="contact-icon">
        <svg width="32" height="32" viewBox="0 0 32 32"><path d="M8 2l5 7-3 3c1.5 4 5 7.5 9 9l3-3 7 5-3 5C15 28 4 17 3 5z" fill="#152842"/></svg>
      </div>
      <div class="contact-text" style="top:10px;">555.214.7730.</div>
    </div>
    <div class="contact-rule" style="top:381px;"></div>

    <div class="contact-row" style="top:396px;">
      <div class="contact-icon">
        <svg width="36" height="32" viewBox="0 0 36 32"><rect x="9" y="1" width="18" height="9" fill="#152842"/><rect x="2" y="11" width="32" height="13" rx="3" fill="#152842"/><rect x="9" y="19" width="18" height="12" fill="#152842" stroke="#98aeb9" stroke-width="2"/></svg>
      </div>
      <div class="contact-text" style="top:10px;">555.214.7741.</div>
    </div>
    <div class="contact-rule" style="top:475px;"></div>

    <div class="contact-row" style="top:494px;">
      <div class="contact-icon">
        <svg width="34" height="24" viewBox="0 0 34 24"><rect x="1" y="1" width="32" height="22" fill="#152842"/><path d="M1 1l16 12L33 1" fill="none" stroke="#98aeb9" stroke-width="2"/></svg>
      </div>
      <div class="contact-text" style="top:10px;">MTEAGUE@BRINDLECRAFT.COM</div>
    </div>
  </section>

  <section class="collection-side">
    <div class="mirror-frame-art" role="img" aria-label="Faint ornate carved mirror frame decoration"></div>
    <div class="intro-label">INTRODUCING</div>
    <div class="collection-name">QUILLMARSH</div>
    <div class="collection-rule left"></div>
    <div class="collection-stars">****</div>
    <div class="collection-rule right"></div>
    <div class="collection-features">EXCULUSIVE DESIGN<br>LIMITED DISTRIBUTION<br>GENEROUS PROPORTION</div>
    <div class="collection-dates">LIMITED INTRODUCTION<br>OCTOMBER 2015<br>FULL COLLECTION LAUNCHED<br>APRIL 2016</div>
  </section>

</main>
</body>
</html>
```